載内容詳細に関しては、別添のExcel資料を参照してください。

・ターゲット
BtoB
木工架装を出来る業者を探している車のリース販売会社の担当様

・カラーイメージ
木目デザインと企業カラーである紺色を使用してデザインお願いします
▼木目参考
https://www.tomika-kobo.jp/
▼紺参考
https://www.rvm-t.jp/

・デザイン、ムード
木を扱う仕事なので、木目を上手く使ってデザインしてほしい
▼参考

・JQについて
JQのパターン制作は不要です。
1枚目の画像でデザインお願いします

配置やデザイン等はアレンジしていただいて構いません。
また、縦に制限はありません。

レスポンシブデザインのサイトで、bootstrap4を利用しコーディングする予定になります。

デザイン幅は2000px、コンテンツの幅はbootstrap4デフォルトのの1110pxを基準としてください。
ただし、最近のデザインの流行を取りいれて、フルワイドや、1200~15000px程度の幅のコンテンツをバランスよくレイアウトしてください。
コンテンツ配置は基本12分割になります。がデザインによっては、多少逸脱してもかまいません。
bootstrap4、12分割グリッドの基準のPSDも資料として添付しております。
ご参考になさってください。

本分のフォントはゴシック系は游ゴシック、メイリオ、明朝系は遊明朝でお願いします。
飾り文字はフリーフォントか、googleフォントを利用してください。

メイン画像部分・グローバルメニューは、ワイド適用でお願いします。

不明点、質問などありましたらメッセージ等でご連絡ください。
1ページ
青系、水色系
• 高解像度JPG (.jpg)
• フォトショップ形式 (.psd)
・資料上はサイト名(社名)や住所などは伏字にしております。
ご提案時点ではそのまま作成をお願いします。

・使用画像は当選後こちらで用意します。
ご提案時点では前項同様に、カンプデータ等をご使用のうえ、当選後に本内容へ差し替え修正をお願いします。
また、雰囲気が合っていれば、指定外の画像を追加掲載いただいてOKです。

・当選前提となった方は正式な社名及び連絡先をお伝えしますので修正対応をお願いします。
また希望の際は、当選後、中ページの制作及びコーディングも別途ご依頼可能です。

```html
<!DOCTYPE html>
<html lang="ja">
<head>
<meta charset="utf-8">
<title>木工架装の専門業者 ○○○○○</title>
<link rel="stylesheet" href="https://fonts.googleapis.com/css2?family=Great+Vibes&family=Noto+Sans+JP:wght@400;500;700&family=Noto+Serif+JP:wght@400;500;600&display=swap">
<style>
:root{
  --navy:#1d2b5a;
  --navy-dark:#142047;
  --wood-light:#f4f1ec;
  --wood-mid:#e9e3da;
  --script:#cbb89c;
  --text:#333;
  --muted:#666;
  --white:#fff;
  --line:#d9d3c9;
}
*{box-sizing:border-box;margin:0;padding:0}
html,body{width:1200px;height:2376px;overflow:hidden}
body{font-family:"Noto Sans JP",sans-serif;color:var(--text);background:var(--wood-light);position:relative}
.serif{font-family:"Noto Serif JP",serif}
.script{font-family:"Great Vibes",cursive;color:var(--script);font-weight:400;position:absolute;line-height:1}
.photo{position:absolute}

/* header */
.site-header{position:absolute;top:0;left:0;width:1200px;height:60px;z-index:3}
.brand{position:absolute;left:16px;top:12px;width:150px;height:120px;background:var(--white);border:1px solid var(--line);padding:18px 12px 0;text-align:center}
.brand-mark{width:14px;height:14px;background:var(--navy);margin:0 auto 6px}
.brand-sub{font-size:9px;color:var(--navy);letter-spacing:.05em}
.brand-name{font-family:"Noto Serif JP",serif;font-size:16px;color:var(--navy);font-weight:600;margin:4px 0 8px;letter-spacing:.1em}
.brand-tag{display:block;background:var(--navy);color:var(--white);font-size:9px;padding:4px 0}
.global-nav{position:absolute;right:24px;top:12px;display:flex;align-items:center;gap:26px;font-size:11px;color:var(--white)}
.global-nav .tel{background:var(--white);color:var(--navy);padding:6px 12px;font-weight:700;display:flex;align-items:center;gap:6px}
.global-nav .current{background:var(--navy);padding:6px 12px}

/* hero */
.hero{position:absolute;top:0;left:0;width:1200px;height:480px}
.hero .photo{inset:0;background:linear-gradient(180deg,#6b6b6e 0%,#3e3f44 30%,#b6865a 55%,#c99563 80%,#8d6a4c 100%)}
.hero-copy{position:absolute;top:136px;left:0;width:1200px;text-align:center;color:var(--white);text-shadow:0 2px 8px rgba(0,0,0,.5)}
.hero-copy h1{font-family:"Noto Serif JP",serif;font-weight:500;font-size:30px;line-height:1.6;letter-spacing:.12em}
.hero-copy p{margin-top:18px;font-family:"Noto Serif JP",serif;font-size:17px;letter-spacing:.15em}
.hero-copy p strong{display:block;font-size:30px;font-weight:500;letter-spacing:.2em;margin-top:2px}

/* intro */
.intro{position:absolute;top:480px;left:0;width:1200px;height:440px;background:linear-gradient(90deg,#f7f5f1,#ece7df 50%,#f6f3ee)}
.intro .script-left{left:14px;top:24px;font-size:44px}
.intro .script-right{right:16px;top:-20px;font-size:22px;color:#efe9df}
.intro-card{position:absolute;left:400px;top:80px;width:400px;height:270px;background:var(--white);padding:28px 34px;text-align:center}
.intro-card h2{font-family:"Noto Serif JP",serif;color:var(--navy);font-size:19px;font-weight:600;line-height:1.55;letter-spacing:.06em}
.intro-card h3{font-family:"Noto Serif JP",serif;color:var(--navy);font-size:14px;font-weight:600;margin-top:14px;line-height:1.6}
.intro-card p{font-size:10px;line-height:2;color:var(--muted);margin-top:12px;text-align:left}

/* business */
.business{position:absolute;top:920px;left:0;width:1200px;height:440px;background:var(--wood-mid)}
.business .photo{left:0;top:0;width:780px;height:420px;background:linear-gradient(160deg,#3a3a3d 0%,#5a5653 30%,#b07a4c 60%,#cf9c68 100%)}
.business .script{right:22px;top:90px;font-size:46px}
.service-card{position:absolute;left:800px;top:160px;width:320px;height:170px;background:var(--white);padding:24px 26px}
.service-card h2{font-family:"Noto Serif JP",serif;color:var(--navy);font-size:17px;font-weight:600}
.service-card p{font-size:10px;color:var(--muted);line-height:1.9;margin-top:10px}
.btn{display:inline-block;background:var(--navy);color:var(--white);font-size:10px;padding:7px 22px;letter-spacing:.1em}
.service-card .btn{margin-top:12px}

/* works */
.works{position:absolute;top:1360px;left:0;width:1200px;height:440px;background:var(--wood-light)}
.works .script{left:20px;top:20px;font-size:50px}
.works h2{position:absolute;top:84px;left:0;width:1200px;text-align:center;font-family:"Noto Serif JP",serif;color:var(--navy);font-size:19px;font-weight:600;letter-spacing:.12em}
.works h2::after{content:"";display:block;width:30px;height:2px;background:var(--navy);margin:8px auto 0}
.works-list{position:absolute;top:128px;left:0;width:1200px;height:250px}
.works-list .photo{top:0;height:250px}
.works .w1{left:0;width:390px;background:linear-gradient(170deg,#4d4d50,#b98656 55%,#d39f6c)}
.works .w2{left:405px;width:390px;background:linear-gradient(170deg,#6e6e70,#a87650 50%,#c8925f)}
.works .w3{left:810px;width:390px;background:linear-gradient(170deg,#8a8985,#c59462 55%,#ddb180)}
.works .btn{position:absolute;left:555px;top:340px;width:90px;text-align:center;padding:7px 0}

/* contact */
.contact{position:absolute;top:1800px;left:0;width:1200px;height:390px;background:linear-gradient(90deg,#f6f3ee,#ebe5dc)}
.contact .script{right:24px;top:42px;font-size:46px}
.contact-card{position:absolute;left:260px;top:110px;width:340px;height:250px;background:var(--white);padding:30px 34px}
.contact-card h2{font-family:"Noto Serif JP",serif;color:var(--navy);font-size:19px;font-weight:600}
.contact-card p{font-size:10px;color:var(--muted);line-height:1.8;margin-top:10px}
.contact-card .tel{margin-top:16px;display:flex;align-items:center;gap:8px;color:var(--navy);font-weight:700;font-size:16px;border:1px solid var(--navy);width:190px;padding:6px 12px}
.contact-card .btn{margin-top:10px;width:190px;text-align:center;padding:9px 0}
.contact .photo{left:600px;top:110px;width:360px;height:250px;background:linear-gradient(140deg,#9a8f80,#c8b59a 40%,#e4d4bb 70%,#b49b7c)}

/* footer */
.site-footer{position:absolute;top:2190px;left:0;width:1200px;height:186px;background:var(--white);border-top:1px solid var(--line)}
.footer-info{position:absolute;left:260px;top:34px;font-size:10px;color:var(--muted);line-height:1.8}
.footer-info strong{display:block;color:var(--navy);font-size:12px;font-weight:700;margin-bottom:4px}
.footer-nav{position:absolute;right:240px;top:34px;display:flex;gap:28px;font-size:10px;color:var(--text)}
.footer-contact{position:absolute;right:240px;top:68px;width:220px;text-align:center;padding:8px 0;border:1px solid var(--navy);color:var(--navy);font-size:10px}
.copyright{position:absolute;left:0;bottom:0;width:1200px;height:26px;line-height:26px;text-align:center;font-size:9px;color:var(--muted);border-top:1px solid var(--line)}
</style>
</head>
<body>

<header class="site-header">
  <div class="brand">
    <div class="brand-mark"></div>
    <div class="brand-sub">木工架装の専門業者</div>
    <div class="brand-name">○○○○○</div>
    <span class="brand-tag">お問い合わせはこちら</span>
  </div>
  <nav class="global-nav">
    <span>ホーム</span>
    <span>業務内容</span>
    <span>施工事例</span>
    <span>会社概要</span>
    <span class="current">お問い合わせ</span>
    <span class="tel">
      <svg width="12" height="12" viewBox="0 0 24 24"><path fill="#1d2b5a" d="M6.6 10.8a15.2 15.2 0 0 0 6.6 6.6l2.2-2.2c.3-.3.7-.4 1-.2 1.1.4 2.3.6 3.6.6.6 0 1 .4 1 1V20c0 .6-.4 1-1 1A17 17 0 0 1 3 4c0-.6.4-1 1-1h3.5c.6 0 1 .4 1 1 0 1.2.2 2.4.6 3.6.1.3 0 .7-.2 1z"/></svg>
      000-000-0000
    </span>
  </nav>
</header>

<section class="hero">
  <div class="photo" role="img" aria-label="ワゴン車の荷室に施工された木製フロア"></div>
  <div class="hero-copy">
    <h1>きめ細かいこだわりと<br>お客様のご要望を叶える確かな技術</h1>
    <p>木工架装の専門業者<strong>○○○○○</strong></p>
  </div>
</section>

<section class="intro">
  <span class="script script-right">Handmade Woodworking</span>
  <span class="script script-left">Woodworking in the car</span>
  <div class="intro-card">
    <h2>車内の木工架装工事なら<br>○○○○○にご相談ください！</h2>
    <h3>"安心・確実"お客様のご要望に<br>細かな技術でお応えいたします</h3>
    <p>当社は車両の荷室や内装に合わせた木工架装を専門に手がけております。一台ごとに寸法を測り、用途に合わせた棚や床をご提案いたします。リース車両の架装もお任せください。丁寧な仕上げと確かな品質で、長く安心してお使いいただける車内をお届けします。</p>
  </div>
</section>

<section class="business">
  <div class="photo" role="img" aria-label="木製の床と棚を架装した車の荷室"></div>
  <span class="script">Business</span>
  <div class="service-card">
    <h2>業務内容</h2>
    <p>車内の床張りや棚の設置など、用途に合わせた木工架装を行います。素材選びから施工まで一貫して対応いたします。</p>
    <span class="btn">詳しく見る</span>
  </div>
</section>

<section class="works">
  <span class="script">Works</span>
  <h2>施工事例</h2>
  <div class="works-list">
    <div class="photo w1" role="img" aria-label="荷室に木製の床を張った施工例"></div>
    <div class="photo w2" role="img" aria-label="荷台に木製の床と側板を取り付けた施工例"></div>
    <div class="photo w3" role="img" aria-label="車内に木製パネルを設置した施工例"></div>
  </div>
  <span class="btn">もっと見る</span>
</section>

<section class="contact">
  <span class="script">Contact</span>
  <div class="contact-card">
    <h2>お問い合せ</h2>
    <p>ご相談・お見積りはお気軽にどうぞ。<br>担当者より折り返しご連絡いたします。</p>
    <div class="tel">
      <svg width="14" height="14" viewBox="0 0 24 24"><path fill="#1d2b5a" d="M6.6 10.8a15.2 15.2 0 0 0 6.6 6.6l2.2-2.2c.3-.3.7-.4 1-.2 1.1.4 2.3.6 3.6.6.6 0 1 .4 1 1V20c0 .6-.4 1-1 1A17 17 0 0 1 3 4c0-.6.4-1 1-1h3.5c.6 0 1 .4 1 1 0 1.2.2 2.4.6 3.6.1.3 0 .7-.2 1z"/></svg>
      000-000-0000
    </div>
    <span class="btn">お問い合わせ</span>
  </div>
  <div class="photo" role="img" aria-label="作業台で木材を加工する職人の手元"></div>
</section>

<footer class="site-footer">
  <div class="footer-info">
    <strong>木工架装の専門業者 ○○○○○</strong>
    〒000-0000 ○○県○○市○○町0-0-0<br>
    TEL 000-000-0000 ／ FAX 000-000-0000
  </div>
  <nav class="footer-nav">
    <span>ホーム</span><span>業務内容</span><span>施工事例</span><span>会社概要</span>
  </nav>
  <div class="footer-contact">お問い合わせはこちら</div>
  <div class="copyright">© ○○○○○ All Rights Reserved.</div>
</footer>

</body>
</html>
```